Modern Design Business Card industrial maintenance company

Business card design for Company named Brookvale Equipment Services

Target Market(s)

Industrial

Industry/Entity Type

Maintenance and repair

Contact Information for Business Card

Place holder for address, office phone, mobile number and email

Requirements
Must have
• Clean modern look
Nice to have
• N/a

```html
<!DOCTYPE html>
<html lang="en">
<head>
<meta charset="utf-8">
<title>Brookvale Equipment Services – Business Card</title>
<link href="https://fonts.googleapis.com/css2?family=Open+Sans:ital,wght@0,400;0,600;0,700;1,600&display=swap" rel="stylesheet">
<style>
  :root {
    --backdrop: #3b3b3b;
    --card: #0c0c0c;
    --silver: #d6d6d6;
    --silver-soft: #b9b9b9;
    --divider: #8a8a8a;
    --gloss: #2f2f2f;
  }
  * { margin: 0; padding: 0; box-sizing: border-box; }
  html, body {
    width: 1200px; height: 801px; overflow: hidden;
    background: var(--backdrop);
    font-family: "Open Sans", sans-serif;
  }
  .sheet {
    width: 1200px; height: 801px;
    display: flex; align-items: center; justify-content: center; gap: 50px;
  }
  .card {
    width: 525px; height: 300px;
    background: var(--card);
    position: relative;
    box-shadow: 0 12px 30px rgba(0,0,0,.45);
  }
  /* front */
  .brand {
    position: absolute; left: 38px; top: 46px;
    display: flex; align-items: center; gap: 14px;
  }
  .brand-mark {
    width: 46px; height: 46px; border-radius: 50%;
    border: 2px solid var(--silver);
  }
  .brand-name {
    color: var(--silver);
    font-weight: 600; font-size: 17px; letter-spacing: 2px;
    text-transform: uppercase; line-height: 1.25;
  }
  .holder {
    position: absolute; left: 38px; top: 150px; width: 210px;
    text-align: right;
  }
  .holder-name {
    color: var(--silver); font-weight: 700; font-size: 19px; letter-spacing: .5px;
    text-transform: uppercase;
  }
  .holder-role {
    color: var(--silver-soft); font-weight: 600; font-style: italic; font-size: 13px;
    margin-bottom: 10px;
  }
  .holder-address {
    color: var(--silver-soft); font-size: 14px; line-height: 1.45;
  }
  .divider {
    position: absolute; left: 268px; top: 140px; width: 1px; height: 112px;
    background: var(--divider);
  }
  .contacts {
    position: absolute; left: 288px; top: 144px;
    list-style: none;
  }
  .contacts li {
    display: flex; align-items: center; gap: 9px;
    color: var(--silver); font-size: 14px; height: 25px;
  }
  .contacts svg { width: 13px; height: 13px; fill: none; stroke: var(--silver); stroke-width: 1.6; }
  /* back */
  .card-back {
    display: flex; flex-direction: column; align-items: center; justify-content: center; gap: 18px;
  }
  .back-mark {
    width: 110px; height: 110px; border-radius: 50%;
    border: 5px solid var(--gloss);
  }
  .back-name {
    color: var(--gloss);
    font-weight: 700; font-size: 24px; letter-spacing: 3px; text-transform: uppercase;
    text-align: center;
  }
</style>
</head>
<body>
<main class="sheet">
  <section class="card card-front">
    <div class="brand">
      <div class="brand-mark"></div>
      <div class="brand-name">Brookvale<br>Equipment Services</div>
    </div>

    <div class="holder">
      <p class="holder-name">Daniel Reyes</p>
      <p class="holder-role">President</p>
      <p class="holder-address">1840 Harbor View Dr<br>Bay City CA 90210</p>
    </div>

    <div class="divider"></div>

    <ul class="contacts">
      <li>
        <svg viewBox="0 0 14 14"><rect x="3.5" y="1" width="7" height="12" rx="1.2"/></svg>
        555-014-2287
      </li>
      <li>
        <svg viewBox="0 0 14 14"><path d="M3 1.5l2.5 2.5-1.5 1.5a8 8 0 0 0 4.5 4.5l1.5-1.5 2.5 2.5-1.5 1.5C6 12.5 1.5 8 1.5 3z"/></svg>
        555-014-2287
      </li>
      <li>
        <svg viewBox="0 0 14 14"><rect x="1" y="3" width="12" height="8.5"/><path d="M1 3l6 5 6-5"/></svg>
        dreyes@brookvale.com
      </li>
      <li>
        <svg viewBox="0 0 14 14"><circle cx="7" cy="7" r="5.8"/><path d="M1.2 7h11.6M7 1.2c-3 3.5-3 8 0 11.6M7 1.2c3 3.5 3 8 0 11.6"/></svg>
        www.brookvale.com
      </li>
    </ul>
  </section>

  <section class="card card-back">
    <div class="back-mark"></div>
    <p class="back-name">Brookvale<br>Equipment Services</p>
  </section>
</main>
</body>
</html>
```